Business card design needed

Chasing a very simplistic modern design with a logo incorporating "TRV".
I'm starting a plumbing business.
I do water, sanitary and drainage plumbing that will cover residential, commercial, rental, rural, excavation, new housing and all maintanence requirements.

Industry/Entity Type

Business

Contact Information for Business Card

TRV PLUMBING SERVICES
DEAN HOLLOWBY - LICENSED PLUMBER
PHONE: 0481926574
E-MAIL: hollodt7@wirelane.com
NORTHERN SUBURBS

Requirements
Must have
• lower case email address

```html
<!DOCTYPE html>
<html lang="en">
<head>
<meta charset="utf-8">
<title>TRV Plumbing Services – Business Card</title>
<link rel="stylesheet" href="https://fonts.googleapis.com/css2?family=Archivo:wdth,wght@110,400;110,500;110,800&display=swap">
<style>
  :root {
    --card-black: #000000;
    --card-white: #ffffff;
    --band-text: #111111;
  }
  html, body {
    margin: 0;
    padding: 0;
    width: 1200px;
    height: 741px;
    overflow: hidden;
    background: var(--card-black);
  }
  .card {
    position: relative;
    width: 1200px;
    height: 741px;
    background: var(--card-black);
    color: var(--card-white);
    font-family: "Archivo", "Helvetica Neue", Arial, sans-serif;
    font-stretch: 110%;
    overflow: hidden;
  }
  .brand-name {
    position: absolute;
    top: -28px;
    right: 8px;
    margin: 0;
    font-size: 178px;
    font-weight: 400;
    line-height: 1;
    letter-spacing: -6px;
    color: var(--card-white);
  }
  .edge-triangle {
    position: absolute;
    left: 0;
    top: 0;
  }
  .details {
    position: absolute;
    left: 283px;
    top: 384px;
  }
  .business-name {
    margin: 0;
    font-size: 46px;
    font-weight: 500;
    line-height: 1;
    letter-spacing: -1px;
  }
  .person-name {
    margin: -4px 0 0;
    font-size: 64px;
    font-weight: 800;
    line-height: 1;
    letter-spacing: 0.5px;
  }
  .person-title {
    display: inline-block;
    margin: 2px 0 0;
    padding-bottom: 3px;
    font-size: 30px;
    font-weight: 400;
    line-height: 1.1;
    border-bottom: 1.5px solid var(--card-white);
    width: 327px;
  }
  .contact-list {
    list-style: none;
    margin: 8px 0 0;
    padding: 0;
    font-size: 32px;
    font-weight: 500;
    line-height: 32px;
  }
  .services-band {
    position: absolute;
    left: 0;
    bottom: 0;
    width: 100%;
    height: 38px;
    background: var(--card-white);
    color: var(--band-text);
    display: flex;
    align-items: center;
    justify-content: center;
    font-size: 24px;
    font-weight: 500;
    letter-spacing: 2px;
    word-spacing: 6px;
  }
</style>
</head>
<body>
  <main class="card">
    <p class="brand-name">TRV</p>

    <svg class="edge-triangle" width="130" height="741" viewBox="0 0 130 741" aria-hidden="true">
      <polygon points="0,400 124,524 0,573" fill="var(--card-white)"/>
    </svg>

    <section class="details">
      <h1 class="business-name">trv plumbing services</h1>
      <h2 class="person-name">Dean Hollowby</h2>
      <p class="person-title">Licensed Plumber</p>
      <ul class="contact-list">
        <li class="contact-phone">Phone: 0481926574</li>
        <li class="contact-email">Email: hollodt7@wirelane.com</li>
        <li class="contact-area">Northern Suburbs</li>
      </ul>
    </section>

    <footer class="services-band">water . sanitary . drainage plumbing</footer>
  </main>
</body>
</html>
```